Business Card Design Project

Need a business card with logo that is attached.
Company name: Moberly Swift Solutions, LLC
My name: Lucia Pembrook
Title: President
Phone number: 703-482-1947
Email: lpembrook@moberlyswiftsolutions.example
web site: www.moberlyswiftsolutions.example

Industry/Entity Type

Business

```html
<!DOCTYPE html>
<html lang="en">
<head>
<meta charset="utf-8">
<title>Moberly Swift Solutions, LLC — Business Card</title>
<link rel="stylesheet" href="https://fonts.googleapis.com/css2?family=Archivo+Black&family=Arimo:wght@700&family=Gelasio&family=Open+Sans:wght@600&display=swap">
<style>
  :root {
    --bg-center: #6a6a6a;
    --bg-mid: #3c3c3c;
    --bg-edge: #161616;
    --panel-light: #2a2a2a;
    --panel-dark: #0c0c0c;
    --ink: #050505;
    --title-ink: #b9b9b9;
    --contact-ink: #a8a8a8;
  }
  html, body {
    margin: 0;
    padding: 0;
    width: 1200px;
    height: 720px;
    overflow: hidden;
    background: var(--bg-edge);
  }
  .card {
    position: relative;
    width: 1200px;
    height: 720px;
    overflow: hidden;
    background: radial-gradient(ellipse 640px 520px at 595px 350px, var(--bg-center) 0%, var(--bg-mid) 55%, var(--bg-edge) 100%);
  }
  .side-panels {
    position: absolute;
    inset: 0;
  }
  .holder {
    position: absolute;
    left: 229px;
    top: 38px;
    transform: translateX(-50%);
    text-align: center;
    font-family: "Arimo", Arial, sans-serif;
    font-weight: 700;
    font-size: 22px;
    line-height: 32px;
    color: var(--title-ink);
    margin: 0;
  }
  .company {
    position: absolute;
    left: 0;
    right: 0;
    top: 160px;
    text-align: center;
    margin: 0;
    color: var(--ink);
  }
  .company-main {
    display: block;
    font-family: "Archivo Black", "Arial Black", sans-serif;
    font-size: 66px;
    line-height: 80px;
    letter-spacing: 1px;
  }
  .company-sub {
    display: block;
    font-family: "Gelasio", Georgia, serif;
    font-weight: 400;
    font-size: 47px;
    line-height: 58px;
  }
  .contact {
    position: absolute;
    left: 0;
    right: 0;
    top: 632px;
    text-align: center;
    font-family: "Open Sans", Arial, sans-serif;
    font-weight: 600;
    font-size: 21px;
    line-height: 30px;
    color: var(--contact-ink);
    margin: 0;
  }
</style>
</head>
<body>
  <div class="card">
    <svg class="side-panels" width="1200" height="720" viewBox="0 0 1200 720">
      <defs>
        <linearGradient id="panelLeft" x1="0" y1="0" x2="1" y2="0">
          <stop offset="0" stop-color="var(--panel-dark)"/>
          <stop offset="1" stop-color="var(--panel-light)"/>
        </linearGradient>
        <linearGradient id="panelRight" x1="1" y1="0" x2="0" y2="0">
          <stop offset="0" stop-color="var(--panel-dark)"/>
          <stop offset="1" stop-color="var(--panel-light)"/>
        </linearGradient>
      </defs>
      <polygon class="panel-left" role="img" aria-label="Dark scratched-metal textured side panel" points="0,40 318,302 318,480 0,720" fill="url(#panelLeft)"/>
      <polygon class="panel-right" role="img" aria-label="Dark scratched-metal textured side panel" points="1200,20 885,306 885,480 1200,720" fill="url(#panelRight)"/>
    </svg>

    <p class="holder">Presedent<br>Lucia Pembrook</p>

    <h1 class="company">
      <span class="company-main">Moberly Swift</span>
      <span class="company-sub">Solutions, LLC</span>
    </h1>

    <p class="contact">
      Phone: 703-482-1947, Email: lpembrook@moberlyswiftsolutions.example<br>
      web site: http://moberlyswiftsolutions.example
    </p>
  </div>
</body>
</html>
```